Startseite gestalten!
Zielgruppe
20 - 45 Jahre alt, legt Wert auf Mode usw.
Hallo,
ich suche jemanden, der mir die Startseite von R&T kavamode (www.rt-kavamode-example.com) chic gestalten kann.
Die Elemente, die jetzt drauf sind sollen bleiben... es geht nur noch um die Gestaltung.
Also Video, Blog und 2 "Werbeflächen" sollen bleiben....
Ebenso die Grundfarbgestaltung usw.
Soll halt schön in die restl. Seite passen.
Freue mich auf die Entwürfe!

```html
<!DOCTYPE html>
<html lang="de">
<head>
<meta charset="utf-8">
<title>R&amp;T kavamode – Startseite</title>
<link rel="stylesheet" href="https://fonts.googleapis.com/css2?family=Arimo:wght@400;700&display=swap">
<style>
  :root {
    --page-bg: #000000;
    --panel: #ffffff;
    --header-top: #3a3a3a;
    --header-bottom: #050505;
    --text: #111111;
    --muted: #6d6d6d;
    --accent: #1e9ae0;
    --rule: #8fcdf0;
    --nav: #ffffff;
    --grass: #5f8a3a;
    --grass-dark: #2f4a1e;
    --shirt: #1a1a1a;
  }
  * { box-sizing: border-box; margin: 0; padding: 0; }
  html, body {
    width: 1200px; height: 1200px; overflow: hidden;
    background: var(--page-bg);
    font-family: "Arimo", Arial, sans-serif;
    color: var(--text);
  }
  .site { position: absolute; left: 195px; top: 193px; width: 810px; height: 813px; }

  .site-header {
    position: absolute; left: 0; top: 0; width: 810px; height: 88px;
    background: linear-gradient(var(--header-top), var(--header-bottom));
  }
  .brand {
    position: absolute; left: 28px; top: 22px; width: 110px;
    color: var(--nav); font-size: 18px; line-height: 21px; font-weight: 700;
    text-align: center; white-space: nowrap;
  }
  .brand span { display: block; }
  .main-nav { position: absolute; top: 42px; left: 0; }
  .main-nav a {
    position: absolute; white-space: nowrap;
    color: var(--nav); text-decoration: none; font-size: 17px;
  }

  .hero { position: absolute; left: 0; top: 88px; width: 810px; height: 182px; display: flex; }
  .hero-photo { height: 100%; position: relative; }
  .hero-photo::after {
    content: ""; position: absolute; left: 0; right: 0; bottom: 0; height: 34px;
    background: linear-gradient(rgba(0,0,0,0), rgba(0,0,0,0.75));
  }
  .hero-photo--left { width: 426px; background: linear-gradient(100deg, #8fb07a 0%, #e8e8e4 35%, #7a5a40 70%, #4f6f33 100%); }
  .hero-photo--right { width: 384px; background: linear-gradient(180deg, #9aa892 0%, #6f8f55 45%, var(--grass) 70%, var(--grass-dark) 100%); }

  .panel { position: absolute; background: var(--panel); border-radius: 9px; }

  .featured { left: 0; top: 273px; width: 584px; height: 258px; }
  .product { position: absolute; top: 15px; height: 132px; border-radius: 4px; }
  .product--longsleeve { left: 93px; width: 120px; background: radial-gradient(ellipse at center, #2a2a2a 45%, #ffffff 72%); }
  .product--bear { left: 246px; width: 120px; background: radial-gradient(ellipse at center, #b88a5a 40%, #ffffff 72%); }
  .product--polo { left: 375px; width: 126px; background: radial-gradient(ellipse at center, #222222 45%, #ffffff 72%); }
  .featured h2 {
    position: absolute; left: 25px; top: 164px;
    color: var(--accent); font-weight: 400; font-size: 27px;
  }
  .featured p {
    position: absolute; left: 25px; top: 203px; width: 540px;
    font-size: 13px; line-height: 18px; text-align: justify;
  }
  .more { color: var(--muted); font-weight: 700; text-decoration: underline; }

  .news { left: 0; top: 543px; width: 584px; height: 202px; }
  .news h2 { position: absolute; left: 25px; top: 12px; font-weight: 400; font-size: 25px; }
  .news-item {
    position: absolute; left: 20px; width: 544px;
    font-size: 13px; line-height: 18px; text-align: justify;
  }
  .news-item time { color: var(--accent); }
  .news-rule { position: absolute; left: 20px; width: 544px; height: 2px; background: var(--rule); }

  .sidebar { left: 597px; top: 273px; width: 213px; height: 472px; }
  .video {
    position: absolute; left: 16px; width: 180px; height: 120px;
    border: 3px solid #111; background: linear-gradient(160deg, #6c8e4d, #3f6a2c 60%, #2c4a1f);
  }
  .video svg { position: absolute; left: 50%; top: 50%; transform: translate(-50%, -50%); }
  .caption { position: absolute; left: 16px; width: 180px; text-align: center; font-size: 10px; color: var(--muted); }

  .promo {
    position: absolute; left: 16px; top: 339px; width: 180px; height: 120px; border-radius: 9px;
    background: linear-gradient(#f2f2f2, #bdbdbd);
  }
  .promo-shirt {
    position: absolute; left: 8px; top: 18px; width: 82px; height: 84px; border-radius: 6px;
    background: linear-gradient(135deg, var(--shirt) 55%, var(--accent) 56%, var(--accent) 70%, var(--shirt) 71%);
  }
  .promo strong { position: absolute; left: 102px; top: 20px; color: var(--accent); font-weight: 400; font-size: 19px; }
  .promo p { position: absolute; left: 102px; top: 46px; width: 72px; font-size: 9px; line-height: 11px; }

  .site-footer {
    position: absolute; left: 0; top: 771px; width: 810px; height: 42px;
    background: linear-gradient(#4a4a4a, #0a0a0a);
    display: flex; justify-content: center; align-items: center; gap: 32px;
  }
  .site-footer a { color: var(--nav); text-decoration: none; font-size: 12px; }
</style>
</head>
<body>
<div class="site">
  <header class="site-header">
    <div class="brand"><span>R&amp;T</span><span>kavamode</span></div>
    <nav class="main-nav">
      <a href="#" style="left:183px">home</a>
      <a href="#" style="left:261px">R&amp;T shop</a>
      <a href="#" style="left:360px">charity</a>
      <a href="#" style="left:441px">über uns</a>
      <a href="#" style="left:539px">impressionen</a>
      <a href="#" style="left:671px">aktualles</a>
    </nav>
  </header>

  <section class="hero">
    <div class="hero-photo hero-photo--left" role="img" aria-label="Polospieler im weißen Trikot auf galoppierendem Pferd"></div>
    <div class="hero-photo hero-photo--right" role="img" aria-label="Zwei Polospieler zu Pferd auf dem Spielfeld"></div>
  </section>

  <section class="panel featured">
    <div class="product product--longsleeve" role="img" aria-label="Schwarzes Langarm-Poloshirt mit Rückennummer 3"></div>
    <div class="product product--bear" role="img" aria-label="Teddybär im weißen Shirt"></div>
    <div class="product product--polo" role="img" aria-label="Schwarzes Kurzarm-Poloshirt mit Rückennummer 3"></div>
    <h2>Lorem ipsum dolor sit amet</h2>
    <p>Lorem ipsum dolor sit amet, consectetur adipisicing elit, sed do eiusmod tempor incididunt ut labore et dolore magna aliqua...<span class="more">+ info</span></p>
  </section>

  <section class="panel news">
    <h2>Aktualles</h2>
    <p class="news-item" style="top:55px"><time>22.09.09</time> Lorem ipsum dolor sit amet, consectetur adipisicing elit, sed do eiusmod tempor incididunt ut labore et dolore magna aliqua...<span class="more">+ info</span></p>
    <div class="news-rule" style="top:95px"></div>
    <p class="news-item" style="top:109px"><time>23.09.09</time> Lorem ipsum dolor sit amet,incididunt ut labore et dolore magna aliqua...<span class="more">+ info</span></p>
    <div class="news-rule" style="top:141px"></div>
    <p class="news-item" style="top:156px"><time>24.09.09</time> Lorem ipsum dolor sit amet, consectetur adipisicing elit...<span class="more">+ info</span></p>
  </section>

  <aside class="panel sidebar">
    <div class="video" style="top:13px" role="img" aria-label="Video: Polospieler im Galopp">
      <svg width="50" height="50" viewBox="0 0 50 50"><circle cx="25" cy="25" r="22" fill="#d9d9d9" fill-opacity="0.85"/><path d="M19 14 L36 25 L19 36 Z" fill="#333"/></svg>
    </div>
    <div class="caption" style="top:138px">Ut enim ad minim veniam</div>
    <div class="video" style="top:168px; height:125px" role="img" aria-label="Video: Polospiel mit mehreren Reitern">
      <svg width="50" height="50" viewBox="0 0 50 50"><circle cx="25" cy="25" r="22" fill="#d9d9d9" fill-opacity="0.85"/><path d="M19 14 L36 25 L19 36 Z" fill="#333"/></svg>
    </div>
    <div class="caption" style="top:297px">Ut enim ad minim veniam</div>
    <div class="promo">
      <div class="promo-shirt" role="img" aria-label="Neues schwarzes T-Shirt mit blauem Schrägband"></div>
      <strong>NEU!</strong>
      <p>Lorem ipsum dolor sit amet, consectetur adipisicing elit</p>
    </div>
  </aside>

  <footer class="site-footer">
    <a href="#">links</a>
    <a href="#">kontakt</a>
    <a href="#">impressum</a>
    <a href="#">AGB</a>
    <a href="#">datenschutzerklärung</a>
  </footer>
</div>
</body>
</html>
```